Recruitment of Luzon Bridge Staffing for the UK market

I want a website for the UK market to attract businesses and companies to come to us for Philipine labour. We want an information site that gives all information on what we do and how we can recruit Philippine labour.
This is a recruitment site for companies to contact us with their requirements for skilled workers coming from the Philipines over to the UK to work.

Target Market(s)

Uk Companies and businesses who want Philipine skilled workers

Industry/Entity Type

REcruitment

Coding

Coded - Design and coding required

Number of Pages Required

5+ page

Font styles to use
Sans Serif

Colors
0054AA
0677BA
7BADD7
CADEEF
E8F1F8
0094D4
00A9DD
6FCCEA
C7EBF8
E9F6FB
EE7325
F08F49
F5BC92
FAE3D3
FDF4ED
EB3D1F
EC4F4E
F09395
F8D3D4
FCEDEE

Requirements
Must have
• Look professional and corperate with drop down menus for Home ,about, services,articles. training , contact us
Nice to have
• Look at Tolvery recruitment- https://tolveryrecruitment.example.co.uk/. This is my current site - https://www.brackwellstaffing.example.com/
Should not have
• Cartoons or silly pictures , needs to be corperate looking

```html
<!DOCTYPE html>
<html lang="en">
<head>
<meta charset="utf-8">
<title>Luzon Bridge Staffing — Skilled Philippine workers for UK companies</title>
<link href="https://fonts.googleapis.com/css2?family=Roboto:wght@400;500;700&display=swap" rel="stylesheet">
<style>
:root{
  --brand-red:#a31f1f;
  --ink:#111111;
  --body:#333333;
  --muted:#666666;
  --line:#d9d9d9;
  --white:#ffffff;
}
*{box-sizing:border-box;margin:0;padding:0}
html,body{width:1200px;height:3176px;overflow:hidden}
body{font-family:'Roboto',sans-serif;color:var(--body);background:var(--white);position:relative}
a{color:inherit;text-decoration:none}

/* header */
.site-header{position:absolute;left:0;top:0;width:1200px;height:63px;background:var(--white)}
.brand{position:absolute;display:flex;align-items:center;gap:8px;font-weight:700;color:var(--brand-red);white-space:nowrap}
.brand-mark{width:14px;height:14px;background:var(--brand-red)}
.site-header .brand{left:117px;top:18px;font-size:20px}
.main-nav{position:absolute;top:21px;left:663px;display:flex;gap:27px;font-size:16px;color:var(--ink)}
.btn-dark{position:absolute;left:942px;top:10px;width:145px;height:43px;background:#000;color:#fff;font-size:16px;font-weight:500;display:flex;align-items:center;justify-content:center}

/* hero */
.hero{position:absolute;left:0;top:63px;width:1200px;height:616px;background:linear-gradient(135deg,#6a5440 0%,#4a4038 35%,#3a3c46 65%,#25272e 100%)}
.hero-title{position:absolute;left:0;top:352px;width:1200px;text-align:center;color:#fff;font-size:37px;font-weight:500;line-height:50px}
.btn-red{position:absolute;background:var(--brand-red);color:#fff;font-weight:500;display:flex;align-items:center;justify-content:center}
.hero .btn-red{left:528px;top:478px;width:144px;height:42px;font-size:18px}

/* about */
.photo{position:absolute}
.about-photo-1{left:112px;top:719px;width:425px;height:356px;background:linear-gradient(135deg,#8a9ab0,#d9c9b5 55%,#b36a4a)}
.about-photo-2{left:319px;top:908px;width:272px;height:214px;background:#fff;padding:4px}
.about-photo-2 div{width:100%;height:100%;background:linear-gradient(135deg,#6f95bf,#a9c1dc 60%,#c9a88a)}
.about-title{position:absolute;left:647px;top:752px;width:430px;font-size:38px;font-weight:500;color:var(--ink);line-height:46px}
.about-text{position:absolute;left:647px;top:864px;width:412px;font-size:15px;line-height:25px;color:var(--body)}
.about .btn-red{left:647px;top:1023px;width:145px;height:42px;font-size:18px}

/* steps */
.steps{position:absolute;left:0;top:1158px;width:1200px;height:341px;display:flex;gap:2px;background:#fff}
.step{flex:1;position:relative;color:#fff}
.step:nth-child(1){background:linear-gradient(160deg,#6b5a4a,#2a2420 70%,#1a1512)}
.step:nth-child(2){background:linear-gradient(160deg,#3f8f90,#2a5d62 60%,#172a2e)}
.step:nth-child(3){background:linear-gradient(160deg,#9a9a9a,#555 60%,#222)}
.step:nth-child(4){background:linear-gradient(160deg,#b9a690,#6c5a49 60%,#251d16)}
.step-body{position:absolute;left:45px;width:218px;bottom:30px}
.step-num{font-size:44px;line-height:44px}
.step-title{font-size:22px;font-weight:500;margin-top:4px}
.step-text{font-size:10.5px;line-height:15px;margin-top:8px}
.step-link{display:inline-block;font-size:10.5px;margin-top:6px;border-bottom:1px solid #fff;line-height:13px}

/* services */
.card{position:absolute;top:1537px;width:289px;height:376px;border:1px solid var(--line);background:#fff;text-align:center}
.card-img{height:209px}
.card h3{margin-top:22px;font-size:15px;font-weight:500;color:var(--brand-red)}
.card p{margin:16px 30px 0;font-size:10px;line-height:15px;color:var(--muted)}
.card .link{position:absolute;left:0;right:0;top:333px;font-size:11px;color:var(--ink);text-decoration:underline}

/* stats */
.stats{position:absolute;left:0;top:1954px;width:1200px;height:297px;background:linear-gradient(120deg,#242424,#2e2c2a 50%,#1e1e1e)}
.stat{position:absolute;top:93px;width:174px;height:107px;border:1px solid rgba(255,255,255,.25);color:#fff;text-align:center}
.stat b{display:block;margin-top:28px;font-size:30px;font-weight:500;line-height:32px}
.stat span{font-size:11px;color:#ddd}

/* blog */
.section-title{position:absolute;left:0;width:1200px;text-align:center;font-size:37px;font-weight:500;color:var(--ink)}
.post{position:absolute;top:2357px;width:289px;height:324px;color:#fff}
.post p{position:absolute;left:30px;right:34px;bottom:35px;font-size:10px;line-height:15px}

/* cta */
.cta{position:absolute;left:0;top:2724px;width:1200px;height:272px;background:linear-gradient(120deg,#2d2f22,#3b3a2c 50%,#1f211a)}
.cta h2{position:absolute;left:0;top:48px;width:1200px;text-align:center;color:#fff;font-size:37px;font-weight:500;line-height:44px}
.btn-white{position:absolute;left:516px;top:164px;width:168px;height:48px;background:#fff;color:var(--ink);font-size:18px;display:flex;align-items:center;justify-content:center}

/* footer */
.site-footer{position:absolute;left:0;top:2996px;width:1200px;height:180px;background:#fff;font-size:12px;color:var(--ink)}
.site-footer .brand{left:133px;top:40px;font-size:20px}
.social{position:absolute;left:131px;top:89px;display:flex;gap:5px}
.social span{width:24px;height:24px;border:1.5px solid var(--ink);border-radius:50%}
.copyright{position:absolute;left:131px;top:125px}
.footer-links{position:absolute;left:385px;top:36px;list-style:none;line-height:22.7px}
.footer-contact{position:absolute;left:491px;top:36px;line-height:22.7px;font-size:11.5px}
.newsletter h4{position:absolute;left:758px;top:34px;font-size:22px;font-weight:500;white-space:nowrap}
.newsletter .field{position:absolute;left:760px;top:75px;width:187px;height:29px;border:1px solid #bbb;font-size:9px;color:#aaa;padding:9px 15px}
.newsletter .send{position:absolute;left:947px;top:75px;width:102px;height:29px;background:#000;color:#fff;font-size:11px;font-weight:500;display:flex;align-items:center;justify-content:center}
</style>
</head>
<body>

<header class="site-header">
  <a class="brand" href="#"><span class="brand-mark"></span>Luzon Bridge Staffing</a>
  <nav class="main-nav"><a href="#">Home</a><a href="#">About</a><a href="#">Blog</a><a href="#">Contact</a></nav>
  <a class="btn-dark" href="#">Get Started</a>
</header>

<section class="hero" role="img" aria-label="Photo of three colleagues reviewing documents together in an office">
  <h1 class="hero-title">Recruiting and placing skilled philippine<br>workers into UK companies</h1>
  <a class="btn-red" href="#">Learn More</a>
</section>

<section class="about">
  <div class="photo about-photo-1" role="img" aria-label="Photo of a supervisor with a clipboard beside a worker in a hard hat"></div>
  <div class="photo about-photo-2"><div role="img" aria-label="Photo of a group of smiling workers in blue uniforms"></div></div>
  <h2 class="about-title">What the business is about</h2>
  <p class="about-text">We source skilled workers directly from the Philippines to work in the UK. With offices , training locations and specialist recruiters we can find the highest quality individuals to add value and resources to any UK buisness. We delivery quality based on vast experience over a number of years.</p>
  <a class="btn-red" href="#">Read More</a>
</section>

<section class="steps">
  <div class="step" role="img" aria-label="Photo of a welder grinding metal with sparks">
    <div class="step-body" style="bottom:42px"><div class="step-num">1</div><div class="step-title">What we do</div><p class="step-text">Our company has been estabilished in the Philippines for over 20 years.</p></div>
  </div>
  <div class="step" role="img" aria-label="Photo of a lab technician in protective gear">
    <div class="step-body"><div class="step-num">2</div><div class="step-title">How we help</div><p class="step-text">We work with companies to find skilled workers that meet the UK requirements for Visas and work permits.</p></div>
  </div>
  <div class="step" role="img" aria-label="Photo of a worker in a high-visibility vest at a desk">
    <div class="step-body" style="bottom:42px"><div class="step-num">3</div><div class="step-title">Where to start</div><p class="step-text">We need to know what your issues are and how we can understand the personnal you require .</p><a class="step-link" href="#">Learn More</a></div>
  </div>
  <div class="step" role="img" aria-label="Photo of a woman working at a laptop in an office">
    <div class="step-body" style="bottom:42px"><div class="step-num">4</div><div class="step-title">Contact us today</div><p class="step-text">Please contact us today with your requirements , this can be care workers ,chef, welders.</p></div>
  </div>
</section>

<section class="services">
  <article class="card" style="left:131px">
    <div class="card-img" role="img" aria-label="Photo of two engineers inspecting machined parts" style="background:linear-gradient(135deg,#7a8590,#c9ccd0 60%,#8f8a84)"></div>
    <h3>UK Skilled Workers List</h3>
    <p>The UK government since brexit have developed a new system based on points (similar to Australia) when recruiting from outside of the UK.</p>
    <a class="link" href="#">Learn More</a>
  </article>
  <article class="card" style="left:456px">
    <div class="card-img" role="img" aria-label="Photo of three young professionals standing in an office" style="background:linear-gradient(135deg,#5e6670,#b8bec6 60%,#6d7782)"></div>
    <h3>Sponsor Licence</h3>
    <p>If you have areas of your business that meet the entry requirements of skilled labour your next step is to gain a sponsor licence for your business.</p>
    <a class="link" href="#">Learn More</a>
  </article>
  <article class="card" style="left:781px">
    <div class="card-img" role="img" aria-label="Photo of a nurse assisting an elderly man" style="background:linear-gradient(135deg,#3d5f9a,#b7c3cf 55%,#6c9b8a)"></div>
    <h3>Recruitment Timeline</h3>
    <p>Brief us on the job profiles – this is passed on to our teams in the Philippines. Our teams in the Philippines source suitable candidates.</p>
    <a class="link" href="#">Learn More</a>
  </article>
</section>

<section class="stats" role="img" aria-label="Dark background photo of colleagues giving a high five">
  <div class="stat" style="left:217px"><b>220</b><span>Opening Job</span></div>
  <div class="stat" style="left:422px"><b>32k</b><span>Fortune Companies</span></div>
  <div class="stat" style="left:624px"><b>300</b><span>Happy Customers</span></div>
  <div class="stat" style="left:829px"><b>50M</b><span>Job Applied</span></div>
</section>

<section class="blog">
  <h2 class="section-title" style="top:2283px">Recent blog entries</h2>
  <article class="post" style="left:131px;background:linear-gradient(180deg,#4e6a4e,#8a8a80 50%,#111)" role="img" aria-label="Photo of a factory worker in a yellow hard hat">
    <p>Lorem ipsum dolor sit amet, consectetur adipiscing elit, sed do eiusmod tempor incididunt ut labore et dolore magna aliqua.</p>
  </article>
  <article class="post" style="left:465px;background:linear-gradient(180deg,#8a4a2a,#3c5b9a 50%,#111)" role="img" aria-label="Photo of two engineers working beside an industrial robot">
    <p>Lorem ipsum dolor sit amet, consectetur adipiscing elit, sed do eiusmod tempor incididunt ut labore et dolore magna aliqua.</p>
  </article>
  <article class="post" style="left:797px;background:linear-gradient(180deg,#5c6e4a,#7a7a8a 50%,#111)" role="img" aria-label="Photo of a carer walking with an elderly woman outdoors">
    <p>Lorem ipsum dolor sit amet, consectetur adipiscing elit, sed do eiusmod tempor incididunt ut labore et dolore magna aliqua.</p>
  </article>
</section>

<section class="cta" role="img" aria-label="Dark background photo of a team outdoors">
  <h2>Bring your team together,<br>whereever they happen to be</h2>
  <a class="btn-white" href="#">Register Now</a>
</section>

<footer class="site-footer">
  <a class="brand" href="#"><span class="brand-mark"></span>Luzon Bridge Staffing</a>
  <div class="social" aria-label="Social links"><span></span><span></span><span></span><span></span></div>
  <p class="copyright">© 2023 Luzon Bridge Staffing Ltd</p>
  <ul class="footer-links"><li>Home</li><li>About us</li><li>Blog</li><li>Contact</li></ul>
  <div class="footer-contact">Contact Details<br>07700 900481<br>sales@luzonbridge.example.com<br>Larkfield Row, Eastmere<br>Eastmere EM4 2 United Kingdom</div>
  <div class="newsletter">
    <h4>Subscribe To Our Newslatter</h4>
    <div class="field">Enter your email</div>
    <div class="send">Subscribe</div>
  </div>
</footer>

</body>
</html>
```